Geschäftspapiere für Software für die Logistikbranche
Zielgruppe
Wir haben eine Software für die Logistikbranche entwickelt. Nutzen dieser Software ist die Digitalisierung von Geschäftsprozessen, eine digitale Tourenvergabe und die Reduktion der Frachtkosten im Unternehmen.
Zielgruppe: B2B, verladendes Gewerbe, jeder der etwas versenden muss
Aufgabenstellung
Die Farbe Orange sollte verwendet werden. Der Briefkopf soll in erster Linie für die Kundenakquise genutzt werden. In zweiter Linie für normale Kommunikation. Die Vorlage sollte etwas für das Auge sein, damit der Text gut zur Geltung kommt. Ein Störer wäre ideal, um Sonderaktionen oder Rabatte in das Anschreiben mit einzubauen.
In der Fußzeile sollten Platzhalter für alle unternehmensbezogenen Daten sein.

```html
<!DOCTYPE html>
<html lang="de">
<head>
<meta charset="utf-8">
<title>Ladepunkt – Briefbogen</title>
<link rel="stylesheet" href="https://fonts.googleapis.com/css2?family=Source+Sans+3:wght@400;600&display=swap">
<style>
  :root {
    --backdrop: #e9e9e9;
    --paper: #f7f7f6;
    --brand-orange: #e0852c;
    --brand-grey: #5a5b5e;
    --mark-faint: #ececeb;
    --footer-text: #ffffff;
  }
  * { box-sizing: border-box; margin: 0; padding: 0; }
  html, body {
    width: 1200px; height: 954px; overflow: hidden;
    background: var(--backdrop);
    font-family: "Source Sans 3", sans-serif;
  }
  .letterhead {
    position: absolute;
    left: 282px; top: 27px;
    width: 636px; height: 900px;
    background: var(--paper);
    box-shadow: 0 6px 24px rgba(0,0,0,0.12);
    overflow: hidden;
  }
  .brand {
    position: absolute;
    left: 58px; top: 62px;
    display: flex; align-items: center; gap: 12px;
  }
  .brand-square {
    width: 34px; height: 34px;
    background: var(--brand-orange);
  }
  .brand-name {
    font-weight: 600;
    font-size: 30px;
    letter-spacing: 0.06em;
    color: var(--brand-orange);
  }
  .background-mark {
    position: absolute;
    left: 300px; top: 330px;
    width: 200px; height: 150px;
    background: var(--mark-faint);
    border-radius: 18px;
  }
  .footer-bands {
    position: absolute;
    left: 0; bottom: 0;
    width: 636px; height: 80px;
  }
  .contact-line {
    position: absolute;
    left: 16px; bottom: 7px;
    display: flex; align-items: center; gap: 16px;
    color: var(--footer-text);
    font-size: 12.5px;
  }
  .contact-item { display: flex; align-items: center; gap: 5px; }
  .contact-item svg { width: 12px; height: 12px; }
  .address {
    position: absolute;
    right: 18px; bottom: 16px;
    color: var(--footer-text);
    font-size: 12.5px;
    line-height: 1.35;
    text-align: left;
  }
</style>
</head>
<body>
  <main class="letterhead">
    <div class="brand">
      <span class="brand-square"></span>
      <span class="brand-name">LADEPUNKT</span>
    </div>

    <div class="background-mark"></div>

    <svg class="footer-bands" viewBox="0 0 636 80" aria-hidden="true">
      <polygon points="0,52 520,52 496,80 0,80" fill="var(--brand-orange)"/>
      <polygon points="500,0 636,0 636,80 484,80 494,52 500,52" fill="var(--brand-grey)"/>
    </svg>

    <div class="contact-line">
      <span class="contact-item">
        <svg viewBox="0 0 12 12"><path d="M2.5 1 L4.5 1 L5.2 3.6 L4 4.6 C4.6 6 5.8 7.3 7.3 8 L8.3 6.8 L11 7.5 L11 9.6 C11 10.4 10.4 11 9.6 11 C5 10.7 1.3 7 1 2.4 C1 1.6 1.7 1 2.5 1 Z" fill="#fff"/></svg>
        01234/56789-00
      </span>
      <span class="contact-item">
        <svg viewBox="0 0 12 12"><rect x="0.8" y="2.3" width="10.4" height="7.4" fill="none" stroke="#fff" stroke-width="1.1"/><path d="M0.8 2.3 L6 6.5 L11.2 2.3" fill="none" stroke="#fff" stroke-width="1.1"/></svg>
        info@ladepunkt-beispiel.de
      </span>
      <span class="contact-item">
        <svg viewBox="0 0 12 12"><circle cx="6" cy="6" r="5" fill="none" stroke="#fff" stroke-width="1"/><ellipse cx="6" cy="6" rx="2.2" ry="5" fill="none" stroke="#fff" stroke-width="0.9"/><path d="M1 6 H11 M2 3.5 H10 M2 8.5 H10" stroke="#fff" stroke-width="0.8"/></svg>
        www.ladepunkt-beispiel.de
      </span>
    </div>

    <address class="address" style="font-style: normal;">
      Musterweg 12<br>
      12345 Beispielstadt
    </address>
  </main>
</body>
</html>
```